Email marketing template

Job type:
Email marketing

Task description:
We would like to send an E-card to our clients wishing them a Merry Christmas

Copy for email marketing:

Seasons Greetings from everyone at RLT…

This year we are supporting our chosen charities by making a donation to help them continue their hard work making a difference. Have a look at our website to find more about the chosen charities we are supporting this Christmas:

http://www.roslyntarbet.example/Our-Approach/Brightfield

Best wishes,

The RLT team

Logo text:
RLT

Descriptive words:
Fun
Playful
Bold
Festive

Deadline:
Monday 16th December

Other information:
We will require you to provide us with HTML coding and uploading to Post Wren. We will then process payment upon testing final materials.

Industry/Entity Type

Marketing

```html
<!DOCTYPE html>
<html lang="en">
<head>
<meta charset="utf-8">
<title>Seasons Greetings from everyone at RLT</title>
<link rel="stylesheet" href="https://fonts.googleapis.com/css2?family=Pinyon+Script&family=Great+Vibes&family=Cormorant+Garamond:ital,wght@1,600&display=swap">
<style>
  :root {
    --paper: #ffffff;
    --damask-light: #f1f0ee;
    --damask-mid: #dddcd8;
    --damask-deep: #d2d1cd;
    --leaf-green: #74bf3f;
    --leaf-green-dark: #5fa62f;
    --script-grey: #8d9195;
    --ink: #111111;
  }
  html, body {
    margin: 0;
    padding: 0;
    width: 1200px;
    height: 1000px;
    overflow: hidden;
    background: var(--paper);
  }
  .ecard {
    position: relative;
    width: 1200px;
    height: 1000px;
    overflow: hidden;
  }
  .damask-backdrop {
    position: absolute;
    inset: 0;
    background:
      radial-gradient(ellipse 70% 60% at 50% 44%, var(--damask-light) 0%, var(--damask-mid) 70%, var(--damask-deep) 100%);
  }
  .plaque {
    position: absolute;
    left: 0;
    top: 0;
    width: 1200px;
    height: 1000px;
  }
  .greeting {
    position: absolute;
    margin: 0;
    white-space: nowrap;
    line-height: 1;
    font-weight: 400;
  }
  .greeting--seasons {
    left: 300px;
    top: 278px;
    font-family: "Pinyon Script", cursive;
    font-size: 64px;
    letter-spacing: 28px;
    color: var(--script-grey);
  }
  .greeting--main {
    left: 388px;
    top: 352px;
    font-family: "Great Vibes", cursive;
    font-size: 120px;
    letter-spacing: 10px;
    color: var(--leaf-green);
  }
  .sender {
    position: absolute;
    left: 316px;
    top: 470px;
    margin: 0;
    display: flex;
    align-items: baseline;
    gap: 16px;
    white-space: nowrap;
    line-height: 1;
  }
  .sender__line {
    font-family: "Pinyon Script", cursive;
    font-size: 40px;
    color: var(--script-grey);
  }
  .sender__name {
    font-family: "Cormorant Garamond", serif;
    font-style: italic;
    font-weight: 600;
    font-size: 56px;
    color: var(--script-grey);
  }
  .web-address {
    position: absolute;
    left: 0;
    width: 1190px;
    top: 572px;
    margin: 0;
    line-height: 1;
    text-align: center;
    font-family: "Cormorant Garamond", serif;
    font-style: italic;
    font-weight: 600;
    font-size: 34px;
    color: var(--ink);
  }
</style>
</head>
<body>
  <main class="ecard">
    <div class="damask-backdrop" role="img" aria-label="Soft grey damask ornamental pattern on white"></div>

    <svg class="plaque" viewBox="0 0 1200 1000" aria-hidden="true">
      <defs>
        <filter id="plaque-shadow" x="-10%" y="-10%" width="120%" height="130%">
          <feDropShadow dx="3" dy="6" stdDeviation="5" flood-color="#000" flood-opacity="0.35"/>
        </filter>
      </defs>
      <path filter="url(#plaque-shadow)"
            fill="var(--paper)" stroke="var(--leaf-green)" stroke-width="30" stroke-linejoin="round"
            d="M 212 240
               L 577 240 L 600 218 L 623 240 L 988 240
               A 44 44 0 0 0 1032 284
               L 1032 300 Q 1060 330 1058 445 Q 1060 560 1032 590
               L 1032 600
               A 44 44 0 0 0 988 644
               L 623 644 L 600 662 L 577 644 L 212 644
               A 44 44 0 0 0 168 600
               L 168 590 Q 140 560 142 445 Q 140 330 168 300
               L 168 284
               A 44 44 0 0 0 212 240 Z"/>
      <path fill="none" stroke="var(--leaf-green-dark)" stroke-width="2" opacity="0.5"
            d="M 212 255 L 577 255 L 600 233 L 623 255 L 988 255
               A 30 30 0 0 0 1018 285 L 1018 305 Q 1044 335 1042 445 Q 1044 555 1018 585
               L 1018 600 A 30 30 0 0 0 988 630 L 623 630 L 600 647 L 577 630 L 212 630
               A 30 30 0 0 0 182 600 L 182 585 Q 156 555 158 445 Q 156 335 182 305
               L 182 285 A 30 30 0 0 0 212 255 Z"/>
    </svg>

    <h1 class="greeting greeting--seasons">Seasons</h1>
    <p class="greeting greeting--main">Greatings</p>
    <p class="sender">
      <span class="sender__line">From everyone at</span>
      <span class="sender__name">RLT</span>
    </p>
    <p class="web-address">www.roslyntarbet.example</p>
  </main>
</body>
</html>
```